Webdesign für Onlineshop
Zielgruppe
Wir verkaufen in unserem Onlineshop alles zum Thema Wohnen mit dem Schwerpunkt Möbel. Die Hauptzielgruppe ist zwischen 25 und 45 Jahren.
Aufgabenstellung
Wir bevorzugen ein modernes, flaches und aufgeräumtes Design ähnlich wie velm.de / dorano88.de mit dem Fokus auf Preisaggressivität und Rabatte.
- Das Grundlayout muss so bleiben, wie es aktuell ist. Natürlich dürfen einzelne Elemente verschoben / versetzt werden.
- Im Header sollte Platz für eine kleine Werbefläche sein (ähnlich wie der konfigurierbare Kleiderschrank).
- Der Shop basiert auf Magento 1.9.
- Die Rabatte in den Produktdetailseiten müssen genauso aufgebaut sein
- Die Suche sollte in den Header platziert werden und nicht im Menü
- Ein SSL Logo soll im Header platziert weden
- Die Vorteile (Kostenloser Versand, Sicher einkaufen, Kauf auf Rechnung) sollen im Header erscheinen
- Das Design sollte responsive sein
Es wird nur das reine Design ohne Programmierung benötigt.

```html
<!DOCTYPE html>
<html lang="de">
<head>
<meta charset="utf-8">
<title>quellmark3berg – Möbel Online Shop</title>
<link href="https://fonts.googleapis.com/css2?family=Raleway:wght@300;400;500;600;700&display=swap" rel="stylesheet">
<style>
:root{
  --green:#7cb03a;
  --green-dark:#6a9a2e;
  --text:#555;
  --muted:#888;
  --line:#e3e3e3;
  --topbar:#f3f3f3;
  --grey-band:#ececec;
  --footer:#3b3b3b;
  --footer-bottom:#2c2c2c;
  --white:#fff;
}
*{box-sizing:border-box;margin:0;padding:0}
html,body{width:1200px;height:2694px;overflow:hidden;background:var(--white)}
body{font-family:"Raleway",sans-serif;color:var(--text);position:relative}
.abs{position:absolute}
.inner{position:absolute;left:234px;width:732px}

/* top bar */
.topbar{position:absolute;left:0;top:0;width:1200px;height:29px;background:var(--topbar);font-size:7.5px;color:var(--muted)}
.topbar .item{position:absolute;top:0;height:29px;display:flex;align-items:center;gap:6px;line-height:1.2}
.topbar .ico{width:12px;height:12px;fill:#bbb}
.topbar .links{color:var(--green);font-size:8.5px}
.topbar .cartbox{position:absolute;right:234px;top:0;width:78px;height:29px;background:var(--green);color:#fff;display:flex;align-items:center;justify-content:space-around;font-size:8px;padding:0 6px}

/* header */
.logo{position:absolute;left:234px;top:34px;display:flex;align-items:center;gap:6px;font-size:22px;font-weight:700;color:var(--green);letter-spacing:-.5px}
.logo .dot{width:12px;height:12px;background:var(--green);border-radius:50%}
.search{position:absolute;left:484px;top:47px;width:293px;height:18px;border:1px solid #c7d9a5}
.search svg{position:absolute;right:4px;top:3px}
.badge-round{position:absolute;top:46px;width:20px;height:20px;border-radius:50%;background:#444;border:3px solid #ddd}
.badge-shield{position:absolute;left:829px;top:40px;width:18px;height:30px;background:#d8d8d8;border-radius:2px 2px 9px 9px}
.promo{position:absolute;left:863px;top:31px;width:104px;height:49px}
.promo .cap{font-size:6.5px;text-transform:uppercase;text-align:center;color:#333;line-height:1.1;font-weight:600}
.promo .img{margin-top:2px;height:26px;background:linear-gradient(90deg,#c8b79a,#ddd0bb 60%,#c54a32);display:flex;align-items:flex-end}
.promo .tag{background:#e8362a;color:#fff;font-size:7px;font-weight:700;padding:1px 3px;width:100%;text-align:right}
.nav{position:absolute;left:234px;top:96px;width:732px;display:flex;justify-content:space-between;font-size:9px;color:var(--green);text-transform:uppercase}
.navline{position:absolute;left:234px;top:82px;width:732px;border-top:1px solid #eee}

/* hero */
.hero{position:absolute;left:0;top:126px;width:1200px;height:423px;background:linear-gradient(90deg,#6b5442 0%,#8a6e57 25%,#4d7c80 45%,#9fb2ae 70%,#d2d6d4 100%)}
.hero h1{position:absolute;top:120px;width:100%;text-align:center;color:#fff;font-weight:400;font-size:45px;line-height:51px;text-transform:uppercase}
.hero .sub{position:absolute;top:262px;width:100%;text-align:center;color:#fff;font-size:24px;text-transform:uppercase}

/* section titles */
.title{font-size:22px;color:var(--green);text-transform:uppercase;font-weight:400}

/* topseller */
.top-list{display:flex;justify-content:space-between}
.top-card{width:170px;font-size:11px;line-height:15px}
.top-card .ph{height:111px;position:relative}
.top-card p{margin-top:19px;height:37px}
.price{color:var(--green);font-weight:600;font-size:11px}
.price s{color:var(--muted);font-weight:400;font-size:9px;margin-right:4px}
.sale{position:absolute;left:0;top:12px;background:var(--green);color:#fff;font-size:10px;padding:4px 7px}
.scroll-track{position:absolute;left:0;top:190px;width:732px;border-top:1px solid var(--line)}
.scroll-thumb{position:absolute;left:125px;top:189px;width:152px;height:3px;background:#ddd}

/* newsletter */
.news{position:absolute;left:234px;top:862px;width:732px;height:166px;display:flex}
.news .ph{flex:1;background:linear-gradient(90deg,#b9c1c8,#d8cbbd 50%,#8a8f95)}
.news .box{width:230px;background:var(--green);border:3px solid var(--green);outline:1px solid #b4d68a;outline-offset:-6px;color:#fff;text-align:center;padding-top:18px}
.news h3{font-size:22px;font-weight:600}
.news .txt{font-size:7.5px;font-weight:600;line-height:11px;margin:14px 22px 0}
.news .mail{margin:14px auto 0;width:183px;height:24px;background:#fff;color:#999;font-size:7.5px;text-align:left;padding:8px 10px;position:relative}

/* beliebte */
.band{position:absolute;left:0;top:1056px;width:1200px;height:314px;background:var(--grey-band)}
.popular{position:absolute;left:234px;top:1151px;width:732px;display:grid;grid-template-columns:repeat(3,250px);row-gap:26px}
.pop{display:flex;gap:9px;height:70px;position:relative;font-size:8.5px;line-height:11px}
.pop .ph{width:107px;height:70px;flex:none}
.pop .info{display:flex;flex-direction:column;justify-content:space-between;padding:4px 0 2px}
.pop .sale{top:6px;left:-6px;font-size:8.5px;padding:3px 6px}

/* tiles */
.tile{position:absolute;overflow:hidden}
.tile .cap{position:absolute;left:19px;color:#fff;font-size:23px;line-height:25px;text-transform:uppercase;font-weight:400}
.framed{border:1px solid #ddd;background:#fff}

/* brands */
.brands{position:absolute;left:234px;top:2191px;width:734px;height:293px;display:grid;grid-template-columns:241px 251px 242px;grid-template-rows:149px 144px}
.brand{display:flex;align-items:center;justify-content:center;color:#333;border-color:var(--line)}
.brand:nth-child(1),.brand:nth-child(2){border-right:1px solid var(--line);border-bottom:1px solid var(--line)}
.brand:nth-child(3){border-bottom:1px solid var(--line)}
.brand:nth-child(4),.brand:nth-child(5){border-right:1px solid var(--line)}

/* footer */
.footer{position:absolute;left:0;top:2537px;width:1200px;height:130px;background:var(--footer);color:#aaa}
.fcol{position:absolute;top:21px}
.fcol h4{font-size:9.5px;color:#eee;font-weight:500;text-transform:uppercase;padding-bottom:7px;border-bottom:1px solid #666}
.fcol ul{list-style:none;font-size:8.5px;line-height:15px;margin-top:9px}
.cert{display:inline-block;width:34px;height:34px;border-radius:50%;background:#d5b44a;border:3px solid #eee;margin-right:11px}
.pay{display:grid;grid-template-columns:repeat(4,34px);gap:5px 10px;margin-top:9px}
.pay span{height:16px;background:#fff;border-radius:2px;color:#2d6ca8;font-size:5.5px;font-weight:700;display:flex;align-items:center;justify-content:center;text-align:center;line-height:6px}
.fbottom{position:absolute;left:0;top:2667px;width:1200px;height:27px;background:var(--footer-bottom);color:#ddd;font-size:7.5px}
</style>
</head>
<body>

<!-- top bar -->
<div class="topbar">
  <div class="item" style="left:234px">
    <svg class="ico" viewBox="0 0 24 24"><path d="M6.6 10.8a15 15 0 006.6 6.6l2.2-2.2a1 1 0 011-.25 11.4 11.4 0 003.6.6 1 1 0 011 1V20a1 1 0 01-1 1A17 17 0 013 4a1 1 0 011-1h3.5a1 1 0 011 1c0 1.25.2 2.45.6 3.6a1 1 0 01-.25 1z"/></svg>
    0541 / 27 41 60 80
  </div>
  <div class="item" style="left:329px">
    <svg class="ico" viewBox="0 0 24 24"><rect x="3" y="5" width="18" height="16" rx="1"/></svg>
    Mo-Fr 9-21 Uhr Sa 10-15 Uhr
  </div>
  <div class="item" style="left:477px">
    <svg class="ico" viewBox="0 0 24 24" style="width:16px"><path d="M1 5h14v11H1zM15 9h5l3 4v3h-8z"/></svg>
    <span>Versandkostenfrei<br>alle Artikel im Online-Shop</span>
  </div>
  <div class="item" style="left:625px">
    <svg class="ico" viewBox="0 0 24 24"><circle cx="12" cy="12" r="10"/></svg>
    <span>0% Finanzierung<br>+ weitere Zahlweisen</span>
  </div>
  <div class="item links" style="left:760px">Zahlungsarten &nbsp;|&nbsp; Lieferung</div>
  <div class="cartbox">
    <span>&#9825; 15</span>
    <span><svg width="12" height="10" viewBox="0 0 24 20" fill="none" stroke="#fff" stroke-width="2"><path d="M1 2h4l3 11h12l3-8H6"/><circle cx="9" cy="17" r="1.5"/><circle cx="18" cy="17" r="1.5"/></svg> 2</span>
  </div>
</div>

<!-- header -->
<div class="logo"><span>quellmark3berg</span><span class="dot"></span></div>
<div class="search">
  <svg width="11" height="11" viewBox="0 0 24 24" fill="none" stroke="#999" stroke-width="2"><circle cx="10" cy="10" r="7"/><path d="M15 15l7 7"/></svg>
</div>
<div class="badge-round" style="left:794px"></div>
<div class="badge-shield"></div>
<div class="promo">
  <div class="cap">Kleiderschrank jetzt auch<br>selbst zusammenstellen</div>
  <div class="img" role="img" aria-label="Konfigurierbarer Kleiderschrank"><div class="tag">10% Einführungsrabatt</div></div>
</div>
<div class="navline"></div>
<nav class="nav">
  <span>Wohnen</span><span>Schlafen</span><span>Kinder-Baby</span><span>Essen</span><span>Küche</span><span>Bis60%Rabatt</span><span>Sonstiges</span><span>Sale</span>
</nav>

<!-- hero -->
<section class="hero" role="img" aria-label="Moderne Einbauküche mit Holzfronten und petrolfarbener Wand">
  <h1>Möbel im Online Shop<br>von quellmark3berg</h1>
  <div class="sub">Einfach und sicher</div>
</section>

<!-- topseller -->
<div class="inner" style="top:596px">
  <h2 class="title">Unsere Topseller</h2>
</div>
<div class="inner" style="top:644px">
  <div class="top-list">
    <div class="top-card">
      <div class="ph" role="img" aria-label="Funktionssofa grün-weiß" style="background:linear-gradient(180deg,#e6e4e0,#b9cf4a 55%,#f2f2f2)"></div>
      <p>Funktionssofa grün-weiß</p>
      <div class="price" style="margin-top:5px">804,00 €</div>
    </div>
    <div class="top-card">
      <div class="ph" role="img" aria-label="Boxspringbett grau" style="background:linear-gradient(180deg,#cfd0d2,#b4b5b8 60%,#8a6b55)"><span class="sale">-30%</span></div>
      <p>Doppelschlafsofa in Kunstleder weiß und Stoff schwarz-grau</p>
      <div class="price"><s>520,00 €</s>334,00 €*</div>
    </div>
    <div class="top-card">
      <div class="ph" role="img" aria-label="Dauerschläfer dunkelgrau" style="background:linear-gradient(180deg,#e1e1df,#3b3b3b 55%,#9a9a98)"></div>
      <p>Dauerschläfer, Dauerschlafsofa in dunkelgrau</p>
      <div class="price">368,00 €</div>
    </div>
    <div class="top-card">
      <div class="ph" role="img" aria-label="Ausziehtisch weiß mit Stühlen" style="background:linear-gradient(180deg,#c7cdd0,#eef0f0 50%,#6f7275)"></div>
      <p>Ausziehtisch 120x80 cm in Hochglanz weiß</p>
      <div class="price">250,17 €</div>
    </div>
  </div>
  <div class="scroll-track"></div><div class="scroll-thumb"></div>
</div>

<!-- newsletter -->
<div class="news">
  <div class="ph" role="img" aria-label="Lächelnde Familie auf einem grauen Sofa"></div>
  <div class="box">
    <h3>5 € GUTSCHEIN</h3>
    <div class="txt">Kostenlosen Newsletter abonnieren, von zahlreichen Aktionen profitieren und zusätzlich 5€ Gutschein sichern!</div>
    <div class="mail">E-mail
      <svg style="position:absolute;right:8px;top:7px" width="16" height="10" viewBox="0 0 16 10" fill="var(--green)"><path d="M3 0h13v10H3zM0 3h2v1H0zM0 6h2v1H0z"/></svg>
    </div>
  </div>
</div>

<!-- beliebte artikel -->
<div class="band"></div>
<div class="inner" style="top:1100px"><h2 class="title">Beliebte Artikel</h2></div>
<div class="popular">
  <div class="pop"><div class="ph" role="img" aria-label="Funktionssofa grün-weiß" style="background:linear-gradient(180deg,#e4e2de,#b9cf4a 55%,#f0f0f0)"></div><div class="info"><span>Funktionssofa grün-weiß</span><span class="price">804,00 €</span></div></div>
  <div class="pop"><span class="sale">-30%</span><div class="ph" role="img" aria-label="Schlafsofa schwarz-grau" style="background:linear-gradient(180deg,#d9d9d9,#3c3c3c 50%,#f2f2f2)"></div><div class="info"><span>Doppelschlafsofa in Kunstleder weiß und Stoff schwarz-grau</span><span class="price"><s>520,00 €</s>334,00 €*</span></div></div>
  <div class="pop"><div class="ph" role="img" aria-label="Funktionssofa grün-weiß" style="background:linear-gradient(180deg,#e4e2de,#b9cf4a 55%,#f0f0f0)"></div><div class="info"><span>Funktionssofa grün-weiß</span><span class="price">804,00 €</span></div></div>
  <div class="pop"><div class="ph" role="img" aria-label="Ecksofa grau in Wohnzimmer" style="background:linear-gradient(180deg,#8f7a64,#6e6a66 55%,#c9c3bb)"></div><div class="info"><span>Funktionssofa grün-weiß</span><span class="price">804,00 €</span></div></div>
  <div class="pop"><div class="ph" role="img" aria-label="Rotes Sofa vor Ziegelwand" style="background:linear-gradient(180deg,#9a8a80,#c9252a 55%,#e9e9e9)"></div><div class="info"><span>Doppelschlafsofa in Kunstleder weiß und Stoff schwarz-grau</span><span class="price"><s>520,00 €</s>334,00 €*</span></div></div>
  <div class="pop"><div class="ph" role="img" aria-label="Ecksofa grau in Wohnzimmer" style="background:linear-gradient(180deg,#8f7a64,#6e6a66 55%,#c9c3bb)"></div><div class="info"><span>Funktionssofa grün-weiß</span><span class="price">804,00 €</span></div></div>
</div>

<!-- tiles -->
<div class="tile framed" style="left:234px;top:1396px;width:231px;height:168px;background:linear-gradient(180deg,#e0e0e0,#c7cf6a 45%,#bdbdbd)" role="img" aria-label="Zwei grüne Barhocker"></div>
<div class="tile framed" style="left:484px;top:1396px;width:231px;height:168px;background:radial-gradient(circle at 50% 45%,#f4f6f8 0,#dde2e7 35%,#fff 60%)" role="img" aria-label="Weiße Blütenleuchte"></div>
<div class="tile" style="left:734px;top:1396px;width:230px;height:283px;background:linear-gradient(160deg,#2d3446,#5c5a5a 40%,#c5c3bf 75%,#8d8a86)" role="img" aria-label="Barhocker an Theke vor Fensterfront">
  <div class="cap" style="top:188px">Immer modern,<br>hochwertig &amp;<br>günstig</div>
</div>
<div class="tile" style="left:234px;top:1580px;width:481px;height:284px;background:linear-gradient(180deg,#9aa6b3,#e9eced 45%,#6d7278)" role="img" aria-label="Weiße Küchenzeile mit Backofen">
  <div class="cap" style="top:203px">Unser großes Möbel<br>Angebot - entdecken<br>Sie die Vielfalt</div>
</div>
<div class="tile framed" style="left:734px;top:1698px;width:230px;height:166px" role="img" aria-label="Kundenservice-Mitarbeiterin mit Headset">
  <div style="position:absolute;left:95px;top:12px;width:90px;height:150px;background:linear-gradient(180deg,#a57555,#f2e2d8 45%,#fff)"></div>
  <div class="cap" style="top:124px;color:var(--green)">Unser Service</div>
</div>
<div class="tile" style="left:234px;top:1886px;width:730px;height:211px;background:linear-gradient(90deg,#a7c4b3,#c9d9cf 35%,#d9cfc0 50%,#e8eae8 70%,#6f9f8f)" role="img" aria-label="Mutter mit Baby neben weißem Kinderbett">
  <div class="cap" style="top:22px">Kindgerecht und<br>schön!</div>
</div>

<!-- brands -->
<div class="inner" style="top:2144px"><h2 class="title">Möbel direkt vom Hersteller</h2></div>
<div class="brands">
  <div class="brand"><span style="font-size:21px;font-weight:300;letter-spacing:1px">FORMHAUS INTERIEUR</span></div>
  <div class="brand"><span style="font-size:22px;font-weight:600;letter-spacing:1px">KANTWERK</span></div>
  <div class="brand"><span style="font-size:13px;letter-spacing:5px">DIE GESTALTER</span></div>
  <div class="brand"><span style="font-size:15px;letter-spacing:1px">HOLM BRANDTBERG</span></div>
  <div class="brand"><span style="font-size:15px;letter-spacing:3px">SUNDVIK MÖBEL</span></div>
  <div class="brand"><span style="font-size:17px">casa lumera</span></div>
</div>

<!-- footer -->
<footer class="footer">
  <div class="fcol" style="left:234px;width:106px"><h4>Über uns</h4><ul><li>Über uns</li><li>Kontakt</li><li>Impressum</li></ul></div>
  <div class="fcol" style="left:359px;width:230px"><h4>Kundenservice</h4>
    <ul style="display:grid;grid-template-columns:125px 100px"><li>Zahlungsarten</li><li>Datenschutz</li><li>Lieferung</li><li>Katalog</li><li>AGB</li><li>Blog</li><li>Widerrufsrecht</li></ul></div>
  <div class="fcol" style="left:610px;width:166px"><h4>Zertifiziert</h4>
    <div style="margin-top:9px"><span class="cert"></span><span class="cert" style="background:#e9b33a"></span><span class="cert" style="background:#2f6fa8;margin-right:0"></span></div></div>
  <div class="fcol" style="left:797px;width:169px"><h4>Zahlungsarten</h4>
    <div class="pay"><span>Über-<br>weisung</span><span>Online-<br>Konto</span><span>Direkt-<br>zahlung</span><span>Rechnung</span><span>Nach-<br>nahme</span><span>Karte</span><span>Kredit-<br>karte</span><span>Finan-<br>zierung</span></div></div>
</footer>
<div class="fbottom">
  <span class="abs" style="left:234px;top:10px">FOLLOW US</span>
  <span class="abs" style="left:291px;top:9px;width:8px;height:8px;border-radius:50%;background:#ddd"></span>
  <span class="abs" style="right:234px;top:10px">Copyright © 2016. All Rights Reserved</span>
</div>

</body>
</html>
```